Australian HR Consultancy Company Brochure (and more!). Our tagline "Start something amazing."

We are a start-up HR and Recruitment consultancy. We have a group of young, passionate and top performing staff who assist companies with driving their workforce productivity, keeping employees happy, hiring fantastic people and ensuring legal compliance across the HR field.

We work across a variety of sectors such as mining, Not for Profits, Finance, Accounting, Health etc so are not pigeon-holed to one particular group. We tend to deal with medium sized businesses.

Our team is professional and corporate but down to earth and approachable. We have unique offerings in terms of our services and our pricing. We deliver exceptional value to our clients and build long term mutually beneficial relationships. We care about giving back to the community and doing the right thing by everyone we deal with.

Our design should communicate that we are corporate and professional but not uptight 'suits', that we are fresh and engaging. Clear, concise, crisp but not cold.

Thinking 6 page brochure.

We have a variety of colours in our logo and tend to lean towards fresh shades of blue and green but are definitely open to other colours such as purple, pink, orange etc. We would prefer the brochure to be in landscape format (like a powerpoint presentation) as apparently that's easier to read? but open to your expert suggestions!

Target Market(s)

Medium sized business across all industries but within the professional area ie finance, mining, health.

Industry/Entity Type

It Company

Colors
33b8a4
33a6d7
0592cd
85cae6
86cfc6
b768aa

Requirements
Must have
• Needs to be editable version as we will be changing our tagline and about us in the new year.

```html
<!DOCTYPE html>
<html lang="en">
<head>
<meta charset="utf-8">
<title>TeamRise – HR Consulting &amp; Professional Staffing Flyer</title>
<link rel="stylesheet" href="https://fonts.googleapis.com/css2?family=Anton&family=Roboto:wght@300;400;500;700&display=swap">
<style>
:root{
  --blue:#0592cd;
  --sky:#33a6d7;
  --teal:#33b8a4;
  --pale-teal:#86cfc6;
  --pale-blue:#85cae6;
  --navy:#1572b6;
  --ink:#2f3640;
  --grey:#e7e8ea;
  --stage:#efeff0;
  --orange:#f26b21;
  --dark:#34495e;
}
*{box-sizing:border-box;margin:0;padding:0}
html,body{width:1200px;height:1200px;overflow:hidden;background:var(--stage);font-family:'Roboto',sans-serif}
.sheet{position:absolute;top:228px;width:575px;height:745px;overflow:hidden;box-shadow:0 4px 14px rgba(0,0,0,.18)}
.sheet--consulting{left:15px;background:var(--grey)}
.sheet--staffing{left:610px;background:var(--blue)}
.layer{position:absolute;left:0;top:0}
.heading{font-family:'Anton',sans-serif;font-weight:400;letter-spacing:.5px}

/* consulting page */
.brand{position:absolute;display:flex;align-items:center;gap:10px;font-family:'Roboto',sans-serif;font-weight:500;color:var(--ink)}
.brand__dot{width:38px;height:38px;border-radius:50%;background:var(--teal)}
.consulting .brand{left:40px;top:48px;font-size:36px}
.about{position:absolute;left:40px;top:115px;width:290px;font-size:10.6px;line-height:14.2px;color:#555;text-align:justify;font-weight:300}
.handshake{position:absolute;left:350px;top:45px;width:210px;height:205px;border-radius:6px;background:linear-gradient(135deg,#f4f5f6,#dfe2e6)}
.ribbon{position:absolute;display:flex;align-items:center;justify-content:center}
.ribbon--consulting{left:150px;top:252px;width:275px;height:48px;background:linear-gradient(#f3f3f3,#cfd2d5);color:var(--sky);font-size:30px;clip-path:polygon(0 0,100% 0,94% 100%,6% 100%)}
.foundations{position:absolute;left:0;top:311px;width:575px;height:197px;background:var(--sky)}
.foundations__panel{position:absolute;left:0;top:8px;width:178px;height:183px;background:var(--blue);clip-path:polygon(0 0,92% 0,100% 50%,92% 100%,0 100%);color:#fff;text-align:center;padding:24px 8px 0 4px}
.foundations__title{font-size:17px;line-height:22px}
.foundations__text{font-size:13.5px;line-height:17.5px;font-weight:300}
.service{position:absolute;width:92px;text-align:center;font-size:10px;line-height:12px;font-weight:300}
.service svg{display:block;margin:0 auto 5px}
.foundations .service{color:#e8f6fd}
.strategic .service{color:#555}
.strategic__intro{position:absolute;left:62px;top:535px;width:130px;text-align:center;color:#333}
.strategic__title{font-size:17px;color:#222}
.strategic__text{font-size:14px;line-height:14px;font-weight:300}

/* staffing page */
.ribbon--staffing{left:98px;top:20px;width:380px;height:44px;background:var(--teal);color:#fff;font-size:27px;clip-path:polygon(0 0,100% 0,96% 100%,4% 100%)}
.hire-pitch{position:absolute;left:70px;top:88px;color:#fff;font-family:'Anton',sans-serif;font-size:15.5px;line-height:20.5px;letter-spacing:.3px}
.staff-list{position:absolute;left:254px;top:80px;list-style:none;color:#fff;font-size:11.6px;line-height:15.6px;font-weight:700}
.staff-list li::before{content:"➲";display:inline-block;width:18px;font-size:10px}
.portrait{position:absolute;left:0;top:213px;width:575px;height:532px;background:linear-gradient(90deg,#d9dcdf 0%,#b9bec3 45%,#8e959c 100%)}
.ribbon--workshop{left:265px;top:205px;width:280px;height:45px;background:var(--teal);color:#fff;font-size:29px;clip-path:polygon(0 0,100% 0,96% 100%,4% 100%)}
.workshop-box{position:absolute;left:283px;top:258px;width:242px;height:247px;background:rgba(90,96,104,.72);color:#fff;padding:6px 6px 0 6px}
.workshop-box__lead{font-family:'Anton',sans-serif;font-size:14px;letter-spacing:.2px}
.workshop-box__text{font-size:10px;line-height:12.3px;font-weight:700;text-align:justify;margin-top:3px}
.workshop-list{list-style:none;margin-top:11px;font-family:'Anton',sans-serif;font-size:16.5px;line-height:24.5px;letter-spacing:.2px}
.workshop-list li::before{content:"✓";color:var(--teal);margin-right:6px;font-family:'Roboto',sans-serif;font-size:13px}
.contact{position:absolute;right:42px;top:555px;text-align:right;color:#fff;font-family:'Anton',sans-serif;text-shadow:0 1px 2px rgba(0,0,0,.35)}
.contact__lead{font-size:10.5px}
.contact__web{font-size:18px;margin-top:2px}
.contact__phone{font-size:24px;margin-top:2px}
.staffing .brand{right:46px;top:652px;font-size:27px;color:#3b4048}
.staffing .brand__dot{width:30px;height:30px}
.team-line{position:absolute;left:28px;top:708px;color:#fff;font-family:'Anton',sans-serif;font-size:12.5px;letter-spacing:.3px}
</style>
</head>
<body>

<!-- HR consulting page -->
<section class="sheet sheet--consulting consulting">
  <svg class="layer" width="575" height="745" viewBox="0 0 575 745" aria-hidden="true">
    <path d="M0 0H575V90C470 35 260 18 0 22Z" fill="var(--blue)"/>
    <path d="M0 22C260 18 470 35 575 90V118C470 55 260 30 0 32Z" fill="var(--teal)"/>
    <path d="M120 311C170 270 260 255 330 255C420 255 470 275 520 311Z" fill="#fff"/>
    <rect x="0" y="508" width="575" height="237" fill="#fff"/>
    <path d="M0 640C120 700 300 728 575 735V745H0Z" fill="var(--pale-teal)"/>
    <path d="M0 600C90 680 230 712 470 728C520 731 560 733 575 734V745H0Z" fill="var(--teal)"/>
    <path d="M0 660C120 715 330 738 575 742V745H0Z" fill="var(--blue)"/>
  </svg>

  <div class="brand"><span class="brand__dot"></span>TeamRise</div>
  <p class="about">TeamRise is an innovative industry leader in the provision of human resources, industrial relations and recruitment managed services. Our unique approach enables us to meet the challenges and demands of a diverse group of a contemporary Australian businesses. We are committed to delivering exceptional service and value that ensures the best outcomes for our long-term business partnerships.</p>
  <div class="handshake" role="img" aria-label="Sketched illustration of two business people shaking hands"></div>

  <div class="ribbon ribbon--consulting heading">HR CONSULTING</div>

  <div class="foundations">
    <div class="foundations__panel">
      <div class="foundations__title heading">HR<br>FOUNDATIONS</div>
      <div class="foundations__text">Building the<br>HR foundations<br>for legal compliance<br>&amp; employee<br>management</div>
    </div>
  </div>

  <!-- foundations services -->
  <div class="service" style="left:181px;top:318px">
    <svg width="52" height="52" viewBox="0 0 52 52"><circle cx="26" cy="26" r="25" fill="var(--orange)" stroke="#fff" stroke-width="2"/><rect x="17" y="13" width="18" height="25" fill="#fde3a7"/><path d="M20 19h12M20 24h12M20 29h9" stroke="#c0502a" stroke-width="1.5"/></svg>
    Employment Contracts &amp; Agreements</div>
  <div class="service" style="left:274px;top:318px">
    <svg width="52" height="52" viewBox="0 0 52 52"><circle cx="26" cy="26" r="25" fill="var(--dark)" stroke="#fff" stroke-width="2"/><path d="M26 26L14 16M26 26L38 16M26 26L14 36M26 26L38 36M26 26V12" stroke="#85cae6" stroke-width="1.5"/><circle cx="26" cy="26" r="5" fill="#f5a623"/><circle cx="14" cy="16" r="3" fill="#85cae6"/><circle cx="38" cy="16" r="3" fill="#85cae6"/><circle cx="14" cy="36" r="3" fill="#85cae6"/><circle cx="38" cy="36" r="3" fill="#85cae6"/></svg>
    Organisational Structure &amp; Design</div>
  <div class="service" style="left:368px;top:318px">
    <svg width="52" height="52" viewBox="0 0 52 52"><circle cx="26" cy="26" r="25" fill="var(--orange)" stroke="#fff" stroke-width="2"/><circle cx="26" cy="20" r="6" fill="#fff"/><path d="M15 36c0-7 5-10 11-10s11 3 11 10Z" fill="#fff"/></svg>
    Terminations &amp; Fair Work Advice</div>
  <div class="service" style="left:460px;top:318px">
    <svg width="52" height="52" viewBox="0 0 52 52"><circle cx="26" cy="26" r="25" fill="var(--teal)" stroke="#fff" stroke-width="2"/><rect x="12" y="14" width="22" height="20" fill="#fff"/><path d="M16 31v-6M21 31v-10M26 31v-8" stroke="var(--teal)" stroke-width="3"/><circle cx="38" cy="20" r="3" fill="#1d2b36"/><rect x="35" y="24" width="6" height="14" fill="#1d2b36"/></svg>
    Performance Management</div>
  <div class="service" style="left:181px;top:423px">
    <svg width="52" height="52" viewBox="0 0 52 52"><circle cx="26" cy="26" r="25" fill="var(--pale-blue)" stroke="#fff" stroke-width="2"/><circle cx="24" cy="19" r="6" fill="#2d5f8a"/><path d="M13 37c0-8 5-11 11-11s11 3 11 11Z" fill="#2d5f8a"/><path d="M29 33l4 4 7-8" stroke="#fff" stroke-width="2.5" fill="none"/></svg>
    Recruitment &amp; On boarding</div>
  <div class="service" style="left:274px;top:423px">
    <svg width="52" height="52" viewBox="0 0 52 52"><circle cx="26" cy="26" r="25" fill="#fff"/><circle cx="26" cy="18" r="8" fill="#4a5560"/><text x="26" y="22" font-size="11" fill="#fff" text-anchor="middle" font-family="Roboto,sans-serif">$</text><path d="M12 34l8-4 6 3 6-3 8 4-8 4h-12Z" fill="#9aa4ad"/></svg>
    Remuneration &amp; Benefits</div>
  <div class="service" style="left:368px;top:423px">
    <svg width="52" height="52" viewBox="0 0 52 52"><circle cx="26" cy="26" r="25" fill="var(--blue)" stroke="#fff" stroke-width="2"/><rect x="18" y="11" width="16" height="20" fill="none" stroke="#fff" stroke-width="1.5"/><path d="M21 17h10M21 21h10M21 25h7" stroke="#fff" stroke-width="1.2"/><rect x="13" y="33" width="26" height="8" rx="4" fill="none" stroke="#fff" stroke-width="1.2"/></svg>
    HR Policies &amp; Procedures</div>
  <div class="service" style="left:460px;top:423px">
    <svg width="52" height="52" viewBox="0 0 52 52"><circle cx="26" cy="26" r="25" fill="#13406b" stroke="#fff" stroke-width="2"/><circle cx="26" cy="18" r="5" fill="#fff"/><path d="M18 31c0-5 4-8 8-8s8 3 8 8Z" fill="#fff"/><rect x="14" y="31" width="24" height="4" fill="#fff"/><path d="M17 35v6M35 35v6" stroke="#fff" stroke-width="2"/></svg>
    Workplace Investigations</div>

  <!-- strategic services -->
  <div class="strategic__intro strategic">
    <div class="strategic__title heading">STRATEGIC HR</div>
    <div class="strategic__text">Driving organisational success through strategic people design.</div>
  </div>
  <div class="strategic">
    <div class="service" style="left:181px;top:527px">
      <svg width="52" height="52" viewBox="0 0 52 52"><circle cx="26" cy="26" r="25" fill="var(--sky)"/><circle cx="26" cy="19" r="5" fill="#fff"/><circle cx="16" cy="22" r="4" fill="#fff"/><circle cx="36" cy="22" r="4" fill="#fff"/><path d="M19 38c0-7 3-10 7-10s7 3 7 10ZM10 37c0-6 3-8 6-8s6 2 6 8ZM30 37c0-6 3-8 6-8s6 2 6 8Z" fill="#fff"/></svg>
      Leadership Development</div>
    <div class="service" style="left:274px;top:527px">
      <svg width="52" height="52" viewBox="0 0 52 52"><circle cx="26" cy="26" r="25" fill="var(--teal)"/><rect x="21" y="12" width="10" height="8" fill="#fff"/><rect x="11" y="30" width="9" height="8" fill="#fff"/><rect x="22" y="30" width="9" height="8" fill="#fff"/><rect x="33" y="30" width="9" height="8" fill="#fff"/><path d="M26 20v5M15 30v-5h22v5M26 25v5" stroke="#fff" stroke-width="1.5" fill="none"/></svg>
      Organisational Design</div>
    <div class="service" style="left:368px;top:527px">
      <svg width="52" height="52" viewBox="0 0 52 52"><circle cx="26" cy="26" r="25" fill="#7d858c"/><circle cx="26" cy="26" r="13" fill="none" stroke="#fff" stroke-width="4"/><path d="M35 14l4 8-9 0Z M17 38l-4-8 9 0Z" fill="#7d858c"/></svg>
      Change Management</div>
    <div class="service" style="left:460px;top:527px">
      <svg width="52" height="52" viewBox="0 0 52 52"><circle cx="26" cy="26" r="25" fill="#8d949a"/><path d="M15 12v12M22 10v14M30 10v14M37 12v12" stroke="#fff" stroke-width="3"/><rect x="12" y="28" width="28" height="10" rx="3" fill="#fff"/></svg>
      Culture Programs</div>
    <div class="service" style="left:181px;top:617px">
      <svg width="52" height="52" viewBox="0 0 52 52"><circle cx="26" cy="26" r="25" fill="var(--orange)"/><circle cx="20" cy="16" r="4" fill="#fff"/><rect x="16" y="21" width="8" height="17" fill="#fff"/><path d="M31 38V14M31 16h8M31 22h6M31 28h8M31 34h6" stroke="#fff" stroke-width="2"/></svg>
      Organisational Capabilities</div>
    <div class="service" style="left:274px;top:617px">
      <svg width="52" height="52" viewBox="0 0 52 52"><circle cx="26" cy="26" r="25" fill="#c4c8cc"/><circle cx="26" cy="16" r="7" fill="none" stroke="#222" stroke-width="1.5"/><path d="M19 16h14M26 9v14" stroke="#222" stroke-width="1"/><circle cx="17" cy="29" r="3" fill="#222"/><circle cx="26" cy="29" r="3" fill="#222"/><circle cx="35" cy="29" r="3" fill="#222"/><path d="M12 40c0-5 2-7 5-7s5 2 5 7ZM21 40c0-5 2-7 5-7s5 2 5 7ZM30 40c0-5 2-7 5-7s5 2 5 7Z" fill="#222"/></svg>
      Executive &amp; Leadership Coaching</div>
    <div class="service" style="left:368px;top:617px">
      <svg width="52" height="52" viewBox="0 0 52 52"><circle cx="26" cy="26" r="25" fill="#cdeeea"/><path d="M12 22l8-6 7 4 10-8" stroke="#2b7fb8" stroke-width="2" fill="none"/><circle cx="18" cy="29" r="3" fill="#2b7fb8"/><circle cx="34" cy="27" r="3" fill="#2b7fb8"/><rect x="15" y="33" width="6" height="9" fill="#2b7fb8"/><rect x="31" y="31" width="6" height="11" fill="#2b7fb8"/></svg>
      Employee Engagement &amp; Retention</div>
    <div class="service" style="left:460px;top:617px">
      <svg width="52" height="52" viewBox="0 0 52 52"><circle cx="26" cy="26" r="25" fill="#fde0c4"/><circle cx="26" cy="23" r="8" fill="#f5a623"/><rect x="22" y="31" width="8" height="7" fill="#555"/><path d="M26 9v4M13 23h4M35 23h4M16 13l3 3M36 13l-3 3" stroke="#f26b21" stroke-width="1.5"/></svg>
      Talent Attraction &amp; Acquisition</div>
  </div>
</section>

<!-- professional staffing page -->
<section class="sheet sheet--staffing staffing">
  <svg class="layer" width="575" height="745" viewBox="0 0 575 745" aria-hidden="true">
    <rect x="0" y="29" width="575" height="3" fill="var(--teal)"/>
  </svg>
  <div class="ribbon ribbon--staffing heading">PROFESSIONAL STAFFING</div>
  <div class="hire-pitch">Start hiring<br>incredible people<br>Matching great<br>organisations<br>to great people</div>
  <ul class="staff-list">
    <li>Executive Search</li>
    <li>Recruitment Processing Outsourcing (RPO)</li>
    <li>Contingent &amp; Retained Services</li>
    <li>Permanent Recruitment</li>
    <li>Recruitment Admin Support</li>
    <li>Manager Interview Training</li>
    <li>Talent Attraction &amp; Acquisition Programs</li>
  </ul>

  <div class="portrait" role="img" aria-label="Photo of a smiling businessman in a dark suit with arms crossed, standing in a bright modern office"></div>

  <svg class="layer" width="575" height="745" viewBox="0 0 575 745" aria-hidden="true">
    <path d="M0 560C40 660 180 690 330 680C450 672 530 665 575 660V745H0Z" fill="var(--pale-teal)"/>
    <path d="M0 600C60 675 200 700 340 694C460 689 540 684 575 682V745H0Z" fill="var(--teal)"/>
    <path d="M0 625C80 690 220 712 360 708C470 705 540 700 575 698V745H0Z" fill="var(--blue)"/>
  </svg>

  <div class="ribbon ribbon--workshop heading">WORKSHOP</div>
  <div class="workshop-box">
    <div class="workshop-box__lead">Let's start developing your team.</div>
    <p class="workshop-box__text">Customised programs designed to make a strategic impact on your organisation and leadership.<br>Presented as 1-1.5 hour' Lunch 'N' Learns', half day or full day workshops as requested across:</p>
    <ul class="workshop-list">
      <li>Leadership Development</li>
      <li>Team Building</li>
      <li>Change Management</li>
      <li>Culture Building</li>
      <li>Management Basics</li>
    </ul>
  </div>

  <div class="contact">
    <div class="contact__lead">Start a conversation with us</div>
    <div class="contact__web">www.teamrise.com.au</div>
    <div class="contact__phone">Call: 1300 555 010</div>
  </div>
  <div class="brand"><span class="brand__dot"></span>TeamRise</div>
  <div class="team-line">Our Leadership Team – Sam, Mia, Tom.</div>
</section>

</body>
</html>
```